Mainpage design for a catalog service
Designers,
We are trying our level best to get in contact with the client and get this project finalized as soon as possible.
Any further updates will be posted on the contest page.
Thank you!
please extend contest
To designers:
The ads on the left and right are not fixed size ads. They may vary in size and shape. If you take a look at the attached picture for kvelma.no you will notice that the actual ad is defined in the background and it takes up all the available space.
RK/PTF/HW Team
Please feel free to use free pictures which are available on the internet in the design. Preferably we want a design with least amount of pictures.
We are looking for simplify and to make a fresher design for the site. The ads on the left and right are floating on the background. You are free to be creative for these ads. they don't need to be aligned vertically with the design or to be constraint to the given space in the prototype picture

```html
<!DOCTYPE html>
<html lang="en">
<head>
<meta charset="utf-8">
<title>DOLVASK.no</title>
<link rel="stylesheet" href="https://fonts.googleapis.com/css2?family=Arimo:wght@400;700&display=swap">
<style>
:root{
  --bg-dark:#1f4a06;
  --bg-mid:#4c8a14;
  --bg-light:#6aa51f;
  --green:#6f9e1a;
  --green-dark:#4d7410;
  --green-light:#9cc43a;
  --accent:#d9f06a;
  --panel:#ffffff;
  --panel-edge:#d7dccc;
  --ad-bg:#f4f4f4;
  --ad-text:#9a9a9a;
  --text:#555;
  --link:#5d8a12;
  --footer:#3a3a3a;
  --footer-dark:#262626;
}
*{margin:0;padding:0;box-sizing:border-box}
html,body{width:1200px;height:778px;overflow:hidden}
body{
  position:relative;font-family:"Arimo",Arial,sans-serif;color:var(--text);
  background:
    repeating-linear-gradient(90deg,rgba(255,255,255,.05) 0 6px,rgba(0,0,0,.05) 6px 12px),
    linear-gradient(90deg,var(--bg-dark) 0%,var(--bg-mid) 25%,var(--bg-light) 50%,var(--bg-mid) 75%,var(--bg-dark) 100%);
}
.abs{position:absolute}
.top-ad{left:187px;top:7px;width:821px;height:108px;background:var(--panel);border:3px solid #e4e8dc;
  display:flex;align-items:center;justify-content:center;font-size:26px;font-weight:700;color:#666}
.nav{left:187px;top:120px;width:821px;height:38px;border-radius:4px;
  background:linear-gradient(var(--green-light),var(--green) 55%,var(--green-dark));
  border:1px solid #b8d872;display:flex;align-items:center;padding:0 10px;font-size:11px;color:#fff}
.nav a{color:#fff;text-decoration:none;margin-right:42px}
.nav .active{background:linear-gradient(#9fb23a,#6c7d18);border:1px solid #c7d86e;padding:5px 12px;color:#e9f5b0;margin-right:30px}
.nav .lang{margin-left:auto;margin-right:0}
.header{left:187px;top:168px;width:821px;height:125px;border-radius:6px;
  background:linear-gradient(var(--green-light),var(--green) 60%,var(--green-dark));border:2px solid #b8d872}
.brand{left:14px;top:8px;width:130px;text-align:center}
.brand .mark{width:76px;height:76px;border-radius:50%;background:#f2f2f2;margin:0 auto 4px;border:3px solid #d9d9d9}
.brand .name{font-size:19px;font-weight:700;color:#fff}
.welcome{left:267px;top:16px;width:350px;color:#fff}
.welcome h1{font-size:19px;font-weight:700;margin-bottom:8px}
.welcome h1 span{color:var(--accent)}
.welcome p{font-size:10.5px;line-height:13px}
.search{display:flex;gap:5px}
.search input{height:21px;border:1px solid #ccc;border-radius:3px;font-family:inherit;font-size:9px;padding:0 8px;color:#aaa}
.search button{width:31px;height:21px;border:1px solid #999;border-radius:3px;background:linear-gradient(#ddd,#999);color:#fff;font-size:10px}
.header .search{position:absolute;left:267px;top:89px}
.header .search input{width:252px}
.ad{width:142px;height:197px;background:var(--ad-bg);border:3px solid #e8ebe2;display:flex;align-items:center;justify-content:center;font-size:17px;font-weight:700;color:var(--ad-text)}
.main{left:336px;top:302px;width:528px;height:408px;background:var(--panel);border-radius:6px;border:3px solid var(--panel-edge)}
.cat-bar{position:absolute;left:7px;top:7px;width:508px;height:48px;border-radius:6px;
  background:linear-gradient(var(--green-light),var(--green) 55%,var(--green-dark));border:1px solid #a9cc5a;
  display:flex;align-items:center;padding-left:14px;font-size:19px;font-weight:700;color:#fff}
.cats{position:absolute;left:19px;display:grid;grid-template-columns:repeat(4,107px);column-gap:21px}
.cats h2{font-size:10.5px;font-weight:700;color:var(--link);border-bottom:1px solid #c9d9a8;padding-bottom:4px;margin-bottom:6px}
.cats h2::after{content:" ›";color:#a3c25a}
.cats li{list-style:none;font-size:9px;line-height:15px;color:#777;padding-left:8px;position:relative}
.cats li::before{content:"-";position:absolute;left:0}
.main .search{position:absolute;left:321px;top:375px}
.main .search input{width:163px}
.footer{left:0;top:715px;width:1200px;height:63px;background:linear-gradient(var(--footer),var(--footer-dark))}
.copy{left:187px;top:45px;font-size:9px;color:#ddd}
.social{left:871px;top:3px;width:144px;height:55px;border-radius:5px;background:linear-gradient(#5a5a5a,#333);border:1px solid #666;display:flex;gap:14px;align-items:center;justify-content:center}
.social span{width:32px;height:32px;border-radius:4px;background:#5a7fb9;border:2px solid #ddd}
.social span:nth-child(2){background:#4fb3df}
.social span:nth-child(3){background:#2f7cb1}
</style>
</head>
<body>
<div class="abs top-ad">Your AD</div>

<nav class="abs nav">
  <a class="active" href="#">Home</a><a href="#">About Us</a><a href="#">Services</a><a href="#">Product</a><a href="#">Contact Us</a>
  <a class="lang" href="#">English ▼</a>
</nav>

<header class="abs header">
  <div class="abs brand"><div class="mark"></div><div class="name">DOLVASK</div></div>
  <div class="abs welcome">
    <h1>Welcome to <span>DOLVASK.no</span></h1>
    <p>Lorem ipsum dolor sit amet, etiam pretium praesent cras sociis, nisi risus, praesent gravida, mattis convallis mi aliquam, mattis lorem integer erat vel. Nisi porta, venenatis ac at, felis luctus. Non odio. Sollicitudin tellus.</p>
  </div>
  <form class="search"><input value="Search"><button type="button">›</button></form>
</header>

<div class="abs ad" style="left:187px;top:302px">AD</div>
<div class="abs ad" style="left:187px;top:509px">AD</div>
<div class="abs ad" style="left:871px;top:302px">AD</div>
<div class="abs ad" style="left:871px;top:509px">AD</div>

<main class="abs main">
  <div class="cat-bar">Categories</div>
  <div class="cats" style="top:74px">
    <div><h2>Lorem Ipsum</h2><ul><li>Lorem Ipsum</li><li>Duis Aptius</li><li>Dolor Si Amet</li><li>Lorem Ipsum</li><li>Duis Aptius</li><li>Dolor Si Amet</li></ul></div>
    <div><h2>Lorem Ipsum</h2><ul><li>Lorem Ipsum</li><li>Duis Aptius</li><li>Dolor Si Amet</li><li>Lorem Ipsum</li><li>Duis Aptius</li><li>Dolor Si Amet</li></ul></div>
    <div><h2>Lorem Ipsum</h2><ul><li>Lorem Ipsum</li><li>Duis Aptius</li><li>Dolor Si Amet</li><li>Lorem Ipsum</li><li>Duis Aptius</li><li>Dolor Si Amet</li></ul></div>
    <div><h2>Lorem Ipsum</h2><ul><li>Lorem Ipsum</li><li>Duis Aptius</li><li>Dolor Si Amet</li><li>Lorem Ipsum</li><li>Duis Aptius</li><li>Dolor Si Amet</li></ul></div>
  </div>
  <div class="cats" style="top:210px">
    <div><h2>Lorem Ipsum</h2><ul><li>Lorem Ipsum</li><li>Duis Aptius</li><li>Dolor Si Amet</li><li>Lorem Ipsum</li><li>Duis Aptius</li><li>Dolor Si Amet</li></ul></div>
    <div><h2>Lorem Ipsum</h2><ul><li>Lorem Ipsum</li><li>Duis Aptius</li><li>Dolor Si Amet</li><li>Lorem Ipsum</li><li>Duis Aptius</li><li>Dolor Si Amet</li></ul></div>
    <div><h2>Lorem Ipsum</h2><ul><li>Lorem Ipsum</li><li>Duis Aptius</li><li>Dolor Si Amet</li><li>Lorem Ipsum</li><li>Duis Aptius</li><li>Dolor Si Amet</li></ul></div>
    <div><h2>Lorem Ipsum</h2><ul><li>Lorem Ipsum</li><li>Duis Aptius</li><li>Dolor Si Amet</li><li>Lorem Ipsum</li><li>Duis Aptius</li><li>Dolor Si Amet</li></ul></div>
  </div>
  <form class="search"><input value="Search"><button type="button">›</button></form>
</main>

<footer class="abs footer">
  <div class="abs copy">Copyright © 2010-2013, DOLVASK.no</div>
  <div class="abs social"><span></span><span></span><span></span></div>
</footer>
</body>
</html>
```